Business Card Design Project

We need a logo design for a new company based in Southern California called "Norvale Security Services, Inc." We install security and camera systems for homeowners and business, to protect their assets.
Updates

Project Deadline Extended
Reason: LOGO Design completes in eight days. Would like that design decided before we finish the business cards. Thanks...

Target Market(s)

Homeowners and business owners looking for additional protection of their assets.

Industry/Entity Type

Security

Font styles to use
Serif

Requirements
Must have
• Company Name
Office# 555-472-3615
Service# 555-472-3616
email: NorvaleSecurity@brimwell.net
address: 48620 Thorncrest Lane Marlowe Springs, CA 91704
Nice to have
• Serving Southern California

```html
<!DOCTYPE html>
<html lang="en">
<head>
<meta charset="utf-8">
<title>Norvale Security Services, Inc. — Business Card</title>
<link rel="stylesheet" href="https://fonts.googleapis.com/css2?family=Cormorant+Garamond:ital,wght@0,500;1,400&display=swap">
<style>
  :root {
    --backdrop: #e6e3df;
    --card-black: #0b0b0b;
    --card-red: #c3163a;
    --ink-light: #f4f1ee;
    --ink-soft: rgba(255, 245, 240, 0.88);
  }
  * { box-sizing: border-box; margin: 0; padding: 0; }
  html, body {
    width: 1200px;
    height: 873px;
    overflow: hidden;
    background: var(--backdrop);
  }
  .canvas {
    position: relative;
    width: 1200px;
    height: 873px;
  }
  .business-card {
    position: absolute;
    left: 390px;
    top: 69px;
    width: 420px;
    height: 735px;
    display: flex;
    flex-direction: column;
    box-shadow: 0 18px 40px rgba(0, 0, 0, 0.25);
  }
  .card-brand {
    flex: 0 0 62%;
    background: var(--card-black);
    display: flex;
    flex-direction: column;
    align-items: center;
    justify-content: center;
    gap: 26px;
  }
  .brand-circle {
    width: 96px;
    height: 96px;
    border: 3px solid var(--ink-light);
    border-radius: 50%;
  }
  .brand-name {
    font-family: "Cormorant Garamond", serif;
    font-weight: 500;
    font-variant: small-caps;
    font-size: 24px;
    letter-spacing: 1.5px;
    color: var(--ink-light);
    white-space: nowrap;
  }
  .card-contact {
    flex: 1;
    background: var(--card-red);
    padding: 44px 26px 0 30px;
    font-family: "Cormorant Garamond", serif;
    font-style: italic;
    font-weight: 400;
    font-size: 15px;
    line-height: 1.9;
    color: var(--ink-soft);
  }
  .contact-list { list-style: none; }
  .contact-list li { white-space: nowrap; }
  .service-area { margin-top: 26px; }
</style>
</head>
<body>
<main class="canvas">
  <article class="business-card">
    <header class="card-brand">
      <div class="brand-circle" aria-hidden="true"></div>
      <h1 class="brand-name">Norvale Security Services, Inc.</h1>
    </header>
    <section class="card-contact">
      <ul class="contact-list">
        <li>Office number: 555-472-3615</li>
        <li>Service number: 555-472-3616</li>
        <li>E-mail: NorvaleSecurity@brimwell.net</li>
        <li>Address: 48620 Thorncrest Lane Marlowe Springs, CA 91704</li>
      </ul>
      <p class="service-area">Serving Southern California</p>
    </section>
  </article>
</main>
</body>
</html>
```